Summit Ridge Institute
Cards and Stationary
Summit Ridge Institute - Education
Creative Brief
Simple
Mark Dellow
CEO
5678 East Sorrel Ave. Las Vegas, NV 89102
mark@summitridgeinstitute.example
www.SummitRidgeInstitute.example
Looking to all types of designs. One sided or 2 sided cards are OK. Be creative. Thanks for submitting!
Use your best judgement.

```html
<!DOCTYPE html>
<html lang="en">
<head>
<meta charset="utf-8">
<title>Summit Ridge Institute – Business Card</title>
<link href="https://fonts.googleapis.com/css2?family=Source+Sans+3:wght@400;600;700&display=swap" rel="stylesheet">
<style>
  :root {
    --backdrop: #e6e6e6;
    --card-white: #ffffff;
    --card-black: #050505;
    --ink: #1a1a1a;
    --accent-red: #c8202b;
    --text-white: #ffffff;
  }
  * { margin: 0; padding: 0; box-sizing: border-box; }
  html, body {
    width: 1200px;
    height: 1075px;
    overflow: hidden;
    background: var(--backdrop);
    font-family: "Source Sans 3", "Helvetica Neue", Arial, sans-serif;
  }
  .stage {
    position: relative;
    width: 1200px;
    height: 1075px;
  }
  .card {
    position: absolute;
    top: 117px;
    width: 490px;
    height: 850px;
    border-radius: 26px;
    overflow: hidden;
    box-shadow: 0 4px 14px rgba(0, 0, 0, 0.18);
  }
  .card--front {
    left: 80px;
    background: var(--card-white);
    color: var(--ink);
  }
  .card--back {
    left: 614px;
    background: var(--card-black);
    color: var(--text-white);
  }
  .brand {
    position: absolute;
    left: 0;
    right: 0;
    display: flex;
    flex-direction: column;
    align-items: center;
    text-align: center;
  }
  .card--front .brand { top: 58px; }
  .card--back .brand { top: 270px; }
  .brand__mark {
    width: 80px;
    height: 80px;
    background: var(--accent-red);
    margin-bottom: 40px;
  }
  .brand__name {
    font-weight: 700;
    font-size: 52px;
    line-height: 1.0;
    letter-spacing: 1px;
    text-transform: uppercase;
  }
  .card--front .brand__name { color: var(--ink); }
  .card--back .brand__name { color: var(--text-white); }

  .person {
    position: absolute;
    top: 466px;
    left: 0;
    right: 0;
    text-align: center;
  }
  .person__name {
    font-size: 36px;
    font-weight: 700;
    color: var(--accent-red);
    line-height: 44px;
  }
  .person__title {
    font-size: 29px;
    font-weight: 400;
    color: var(--ink);
    line-height: 36px;
  }
  .contact {
    position: absolute;
    top: 630px;
    left: 0;
    right: 0;
    text-align: center;
    font-size: 22px;
    line-height: 31px;
    color: var(--ink);
  }
  .contact p { margin: 0; }
  .footer-band {
    position: absolute;
    left: 0;
    bottom: 0;
    width: 490px;
    height: 40px;
  }
  .footer__web {
    position: absolute;
    right: 30px;
    bottom: 7px;
    font-size: 23px;
    line-height: 27px;
    font-weight: 600;
    color: var(--text-white);
  }
</style>
</head>
<body>
  <main class="stage">
    <section class="card card--front" aria-label="Business card front">
      <div class="brand">
        <div class="brand__mark" aria-hidden="true"></div>
        <div class="brand__name">Summit Ridge<br>Institute</div>
      </div>

      <div class="person">
        <div class="person__name">Mark Dellow</div>
        <div class="person__title">CEO</div>
      </div>

      <div class="contact">
        <p>5678 East Sorrel Ave.</p>
        <p>Las Vegas, NV 89102</p>
        <p>Phone : 1-800-555-8640</p>
        <p>Cell : 702-555-3918</p>
        <p>Email : mark@summitridgeinstitute.example</p>
      </div>

      <svg class="footer-band" viewBox="0 0 490 40" aria-hidden="true">
        <rect x="0" y="0" width="490" height="40" fill="#050505"/>
        <polygon points="0,0 74,0 44,40 0,40" fill="#c8202b"/>
        <polygon points="74,0 92,0 62,40 44,40" fill="#ffffff"/>
      </svg>
      <div class="footer__web">www.SummitRidgeInstitute.example</div>
    </section>

    <section class="card card--back" aria-label="Business card back">
      <div class="brand">
        <div class="brand__mark" aria-hidden="true"></div>
        <div class="brand__name">Summit Ridge<br>Institute</div>
      </div>
    </section>
  </main>
</body>
</html>
```